Business card design needed

Want the logo on a medium blue background and a nice funky design. I have my own gym and run one on one personal training and nutrition sessions. want it to look lively.
Updates

Please note I requested my logo on a blue background 

PLEASE NOTE: I already have a logo. It is attached to the order!!

Target Market(s)

over 55s

Industry/Entity Type

Nutrition

Contact Information for Business Card

Front of card : Logo ( on blue background )
Keldra Ashby
Nutrition & Fitness Coach for Seniors
Private gym at : 17 Tindal Crescent, Wembury, Perth, WA 6166
Mob : 0418372651
Email : keldraashby@frelmo.com
"For Seniors by a Senior"

Back of card
B.A. ( Soc.)
Dip. Ed. (Sec.)
Wellness Coach
Cert 4 Personal Trainer
Cert. Nutritition
MOVE ON Facilitator
Ageing Boldly Moving Freely Facilitator
NLP Master

```html
<!DOCTYPE html>
<html lang="en">
<head>
<meta charset="utf-8">
<title>Silver Stride Nutrition &amp; Fitness – Business Card</title>
<link rel="stylesheet" href="https://fonts.googleapis.com/css2?family=Cabin:wght@400;500&family=Open+Sans:ital,wght@0,400;0,700;1,400&display=swap">
<style>
  :root {
    --navy: #12325a;
    --lime: #8dc63f;
    --green: #0a9a48;
    --white: #ffffff;
    --ink: #1d2f6b;
    --tan: #e8c89c;
    --gold: #f5c518;
    --page: #e4e4e4;
  }
  * { box-sizing: border-box; margin: 0; padding: 0; }
  html, body {
    width: 1200px; height: 949px; overflow: hidden;
    background: var(--page);
  }
  .canvas { position: relative; width: 1200px; height: 949px; }
  .card {
    position: absolute; left: 250px; width: 700px; height: 431px;
    overflow: hidden;
  }
  .card--front { top: 28px; background: var(--navy); color: var(--white); font-family: "Open Sans", sans-serif; }
  .card--back { top: 489px; background: var(--white); color: var(--ink); font-family: "Cabin", sans-serif; }

  .stripe { position: absolute; top: 0; right: 3px; width: 28px; height: 100%; background: var(--lime); }
  .stripe__foot { position: absolute; bottom: 0; left: 0; width: 100%; height: 34px; background: var(--green); }

  .brand { position: absolute; left: 62px; top: 48px; display: flex; align-items: center; gap: 14px; }
  .brand__mark { width: 46px; height: 46px; border-radius: 50%; background: var(--white); flex: none; }
  .brand__name { font-family: "Cabin", sans-serif; font-weight: 400; font-size: 31px; line-height: 1.15; color: var(--white); }

  .studio { position: absolute; left: 52px; top: 182px; font-family: "Cabin", sans-serif; font-size: 17px; }
  .motto { position: absolute; left: 52px; top: 211px; font-family: "Cabin", sans-serif; font-size: 17px; color: var(--tan); }

  .contact { position: absolute; right: 60px; top: 286px; text-align: right; }
  .contact__name { font-weight: 700; font-size: 28px; line-height: 1.2; }
  .contact__role { font-style: italic; font-size: 16px; color: var(--gold); margin-top: 1px; }
  .contact__mob { font-size: 23px; margin-top: 6px; }
  .contact__mail { font-size: 17px; margin-top: 2px; }

  .back__tab { position: absolute; left: 0; top: 170px; width: 46px; height: 84px; background: var(--green); }
  .credentials { position: absolute; left: 68px; top: 162px; list-style: none; font-size: 16px; font-weight: 500; line-height: 1.28; }
</style>
</head>
<body>
<main class="canvas">
  <section class="card card--front" aria-label="Business card front">
    <div class="brand">
      <span class="brand__mark"></span>
      <span class="brand__name">Silver Stride<br>Nutrition &amp; Fitness</span>
    </div>
    <p class="studio">Private gym at : 17 Tindal Crescent, Wembury, Perth, WA 6166</p>
    <p class="motto">"For Seniors by a Senior"</p>
    <div class="contact">
      <p class="contact__name">Keldra Ashby</p>
      <p class="contact__role">Nutrition &amp; Fitness Coach for Seniors</p>
      <p class="contact__mob">Mob : 0418372651</p>
      <p class="contact__mail">keldraashby@frelmo.com</p>
    </div>
    <div class="stripe"><div class="stripe__foot"></div></div>
  </section>

  <section class="card card--back" aria-label="Business card back">
    <div class="back__tab"></div>
    <ul class="credentials">
      <li>B.A. ( Soc.) Dip. Ed. (Sec.)</li>
      <li>Wellness Coach Cert 4</li>
      <li>Personal Trainer Cert. Nutritition</li>
      <li>MOVE ON Facilitator Ageing Boldly Moving Freely Facilitator</li>
      <li>NLP Master</li>
    </ul>
    <div class="stripe"></div>
  </section>
</main>
</body>
</html>
```